Mixed Martial Arts gym that is known for high quality athletes, students and training

We need a business card designed that is unique and stands out. Something that is not so dark and boring but looks 'energetic' to those that are given it. The customers that would receive this card would be looking to sign up for martial arts or fitness training and this card is used for corporate sponsorships and networking as well.

Corwin Ashby-Lowe
0455013872 or 0467190534
Level 1, 218 Wexcombe Drive. Brackenvale NSW 2197
corwin@thornlevyquarrantgroup.com.au
www.thornlevyquarrantgroup.com

Training

```html
<!DOCTYPE html>
<html lang="en">
<head>
<meta charset="utf-8">
<title>Corwin Ashby-Lowe — Business Card</title>
<link rel="stylesheet" href="https://fonts.googleapis.com/css2?family=Ubuntu:wght@500&family=Questrial&display=swap">
<style>
  :root {
    --stage: #5b5b5b;
    --card-white: #ffffff;
    --charcoal: #353132;
    --orange: #f7941d;
    --ink: #2f2d2e;
    --muted: #6d6d6d;
    --contact-text: #e9e7e7;
  }
  html, body {
    margin: 0;
    padding: 0;
    width: 1136px;
    height: 1200px;
    overflow: hidden;
    background: var(--stage);
  }
  .card {
    position: absolute;
    left: 68px;
    top: 291px;
    width: 1000px;
    height: 617px;
    background: var(--card-white);
    box-shadow: 0 4px 14px rgba(0,0,0,0.35);
    overflow: hidden;
  }
  .card__identity {
    position: absolute;
    left: 70px;
    top: 166px;
  }
  .card__name {
    margin: 0;
    font-family: "Ubuntu", sans-serif;
    font-weight: 500;
    font-size: 41px;
    color: var(--ink);
    letter-spacing: 0.5px;
    line-height: 1;
  }
  .card__role {
    margin: 10px 0 0;
    font-family: "Questrial", sans-serif;
    font-size: 27px;
    color: var(--muted);
  }
  .brand {
    position: absolute;
    left: 672px;
    top: 82px;
    width: 264px;
    display: flex;
    align-items: center;
    gap: 16px;
  }
  .brand__mark {
    width: 34px;
    height: 34px;
    flex: none;
    background: var(--orange);
  }
  .brand__name {
    font-family: "Ubuntu", sans-serif;
    font-weight: 500;
    font-size: 42px;
    line-height: 1.1;
    color: var(--orange);
  }
  .card__band {
    position: absolute;
    left: 0;
    top: 275px;
    width: 1000px;
    height: 342px;
  }
  .contact {
    position: absolute;
    left: 352px;
    top: 360px;
    margin: 0;
    padding: 0;
    list-style: none;
    font-family: "Questrial", sans-serif;
    font-size: 27px;
    color: var(--contact-text);
  }
  .contact__item {
    display: flex;
    align-items: center;
    height: 36px;
    white-space: nowrap;
  }
  .contact__icon {
    width: 22px;
    height: 22px;
    margin-right: 14px;
    flex: none;
  }
</style>
</head>
<body>
  <article class="card">
    <div class="brand">
      <span class="brand__mark"></span>
      <span class="brand__name">Thornlevy<br>Quarrant</span>
    </div>

    <header class="card__identity">
      <h1 class="card__name">Corwin Ashby-Lowe</h1>
      <p class="card__role">Managing Director</p>
    </header>

    <svg class="card__band" viewBox="0 0 1000 342" aria-hidden="true">
      <rect width="1000" height="342" fill="var(--charcoal)"/>
      <polygon points="0,0 81,0 298,342 0,342" fill="var(--orange)"/>
    </svg>

    <ul class="contact">
      <li class="contact__item">
        <svg class="contact__icon" viewBox="0 0 24 24"><path d="M8 2 L11 7 L9 9 Q10 14 14 16 L16 14 L21 17 L19 21 Q8 21 4 9 Q4 4 8 2Z" fill="var(--orange)"/></svg>
        0467190534
      </li>
      <li class="contact__item">
        <svg class="contact__icon" viewBox="0 0 24 24"><path d="M8 2 L11 7 L9 9 Q10 14 14 16 L16 14 L21 17 L19 21 Q8 21 4 9 Q4 4 8 2Z" fill="var(--orange)"/></svg>
        0455013872
      </li>
      <li class="contact__item">
        <svg class="contact__icon" viewBox="0 0 24 24"><rect x="3" y="6" width="18" height="13" rx="1" fill="none" stroke="var(--orange)" stroke-width="2"/><path d="M3 7 L12 13 L21 7" fill="none" stroke="var(--orange)" stroke-width="2"/></svg>
        corwin@thornlevyquarrantgroup.com.au
      </li>
      <li class="contact__item">
        <svg class="contact__icon" viewBox="0 0 24 24"><circle cx="12" cy="12" r="9" fill="none" stroke="var(--orange)" stroke-width="2"/><ellipse cx="12" cy="12" rx="4" ry="9" fill="none" stroke="var(--orange)" stroke-width="1.6"/><path d="M3 12 H21 M5 7 H19 M5 17 H19" stroke="var(--orange)" stroke-width="1.4"/></svg>
        www.thornlevyquarrantgroup.com
      </li>
      <li class="contact__item">Suite 4, 218 Wexcombe Drive.</li>
      <li class="contact__item">Brackenvale NSW 2197</li>
    </ul>
  </article>
</body>
</html>
```